MapleForge PowerPoint & Letterhead Template

Looking for a striking powerpoint template we can use for internal use, customer presentations, etc. Would love a matching letterhead design. I have attached 2 decks as our current template, plus an example of what we like (2014 Cap Brief.pdf). Please keep our color scheme however.

Requirements
Must have
• We are not looking for a revamp of the content in our current presentation. We are looking for a template we can use going forward for any and all content.

```html
<!DOCTYPE html>
<html lang="en">
<head>
<meta charset="utf-8">
<title>MapleForge Presentation Template</title>
<link href="https://fonts.googleapis.com/css2?family=Roboto:wght@400;500;700;900&family=Open+Sans:wght@400;600;700&display=swap" rel="stylesheet">
<style>
:root{
  --bg:#4a4a4d;
  --blue:#1a8fdc;
  --blue-deep:#1456c4;
  --blue-mid:#2ba3e6;
  --blue-light:#8fd0ec;
  --purple:#5b3aa0;
  --ink:#3d3d42;
  --grey:#e4e4e6;
  --white:#ffffff;
}
*{margin:0;padding:0;box-sizing:border-box}
html,body{width:1200px;height:544px;overflow:hidden;background:var(--bg)}
body{position:relative;font-family:"Open Sans",Arial,sans-serif;color:var(--ink)}
.slide{position:absolute;width:277px;height:156px;background:var(--white);overflow:hidden}
.abs{position:absolute}
.brand{position:absolute;display:flex;align-items:center;gap:2px;font-family:"Open Sans",sans-serif;font-size:6px;color:var(--ink)}
.brand .dot{width:5px;height:5px;border-radius:50%;background:var(--blue)}
.brand.light{color:var(--white)}
.brand.light .dot{background:var(--white)}
.headline{position:absolute;font-family:"Roboto",sans-serif;font-weight:700;font-size:13px;color:var(--ink);line-height:1}
.headline span{color:var(--blue)}
.body{position:absolute;font-size:3px;line-height:1.45;color:var(--ink)}
.body.white{color:var(--white)}
.button{position:absolute;background:var(--blue);color:var(--white);font-size:2.6px;line-height:1.4;padding:4px 5px}
.bar{position:absolute;background:var(--purple);color:var(--white);font-size:2.6px;line-height:1.4;padding:4px 5px}
.title-caps{position:absolute;font-family:"Open Sans",sans-serif;font-weight:700;color:var(--blue);font-size:7.5px;line-height:1.3}
.caption{position:absolute;font-size:3px;font-weight:700;text-align:center;line-height:1.35;color:var(--ink)}
svg{position:absolute;overflow:visible}
</style>
</head>
<body>

<!-- Slide 1: cover -->
<section class="slide" style="left:26px;top:25px;background:linear-gradient(120deg,#1638b0 0%,#1a6fd8 55%,#27a7ea 100%)">
  <div class="abs" role="img" aria-label="Circuit-board cloud illustration with streaming data lines" style="left:20px;top:20px;width:130px;height:130px;background:radial-gradient(ellipse at 50% 45%,rgba(120,200,255,.45),rgba(30,80,200,0) 70%)"></div>
  <div class="brand light" style="left:55px;top:68px;font-size:11px;gap:3px"><span class="dot" style="width:8px;height:8px"></span>mapleforge</div>
  <div class="abs" style="left:172px;top:52px;color:#fff;font-family:'Open Sans',sans-serif;font-size:7.4px;line-height:1.35">
    <div style="font-weight:700">MAPLEFORGE DELIVERS<br>YOUR ENTERPRISE<br>TECHNOLOGY GOALS!</div>
    <div>Unleash our expertise<br>to deliver your mission<br>objectives!</div>
  </div>
</section>

<!-- Slide 2: headline with icon column -->
<section class="slide" style="left:316px;top:25px">
  <div class="headline" style="left:33px;top:42px">Head<span>Line</span></div>
  <p class="body" style="left:33px;top:57px;width:108px">Lorem ipsum dolor sit amet, consectetur adipiscing elit, sed do eiusmod tempor incididunt ut labore et dolore magna aliqua. Ut enim ad minim veniam, quis nostrud exercitation ullamco laboris nisi ut aliquip ex ea commodo consequat. Duis aute irure dolor in reprehenderit in voluptate velit esse cillum dolore eu fugiat nulla pariatur. Excepteur sint occaecat cupidatat non proident, sunt in culpa qui officia deserunt mollit anim id est laborum.</p>
  <div class="button" style="left:33px;top:90px;width:70px">Lorem ipsum dolor sit amet, consectetur adipiscing elit, sed do eiusmod tempor aliqua.</div>
  <svg style="left:33px;top:118px" width="9" height="9"><path d="M1 1h8v8M9 1L1 9" stroke="#3d3d42" stroke-width=".8" fill="none"/></svg>
  <div class="brand" style="left:7px;top:145px"><span class="dot"></span>mapleforge</div>
  <div class="abs" style="left:155px;top:0;width:122px;height:156px;background:linear-gradient(160deg,#1a7fd6,#1496e0)">
    <svg width="122" height="156">
      <g fill="none" stroke="#fff" stroke-width=".8">
        <circle cx="30" cy="24" r="7"/><circle cx="30" cy="61" r="7"/><circle cx="30" cy="98" r="7"/><circle cx="30" cy="135" r="7"/>
        <path d="M18 42h24M18 79h24M18 116h24"/>
      </g>
    </svg>
    <p class="body white" style="left:52px;top:20px;width:62px;font-size:2.5px">Lorem ipsum dolor sit amet, consectetur adipiscing elit, sed do eiusmod tempor aliqua.</p>
    <p class="body white" style="left:52px;top:57px;width:62px;font-size:2.5px">Lorem ipsum dolor sit amet, consectetur adipiscing elit, sed do eiusmod tempor aliqua.</p>
    <p class="body white" style="left:52px;top:94px;width:62px;font-size:2.5px">Lorem ipsum dolor sit amet, consectetur adipiscing elit, sed do eiusmod tempor aliqua.</p>
    <p class="body white" style="left:52px;top:131px;width:62px;font-size:2.5px">Lorem ipsum dolor sit amet, consectetur adipiscing elit, sed do eiusmod tempor aliqua.</p>
  </div>
</section>

<!-- Slide 3: numbered list -->
<section class="slide" style="left:607px;top:25px">
  <div class="brand" style="left:234px;top:7px"><span class="dot"></span>mapleforge</div>
  <div class="abs" style="left:0;top:34px;width:215px;height:92px;background:var(--blue)"></div>
  <div class="abs" style="left:82px;top:26px;width:155px;height:15px;background:var(--purple);color:#fff;font-family:Roboto,sans-serif;font-weight:500;font-size:8px;text-align:center;line-height:15px">Lorem Ipsum Dolor Sit</div>
  <svg style="left:227px;top:45px" width="9" height="9"><path d="M1 1h8v8M9 1L1 9" stroke="#3d3d42" stroke-width=".8" fill="none"/></svg>
  <svg width="277" height="156">
    <g fill="#fff"><circle cx="20" cy="57" r="9.5"/><circle cx="20" cy="85" r="9.5"/><circle cx="20" cy="113" r="9.5"/>
    <circle cx="121" cy="55" r="8"/><circle cx="121" cy="83" r="8"/><circle cx="121" cy="112" r="8"/></g>
    <g fill="none" stroke="#1a8fdc" stroke-width=".7"><circle cx="121" cy="55" r="4"/><circle cx="121" cy="83" r="4"/><circle cx="121" cy="112" r="4"/></g>
    <g font-family="Roboto" font-weight="700" font-size="11" fill="#1a6fd0" text-anchor="middle"><text x="20" y="61">01</text><text x="20" y="89">02</text><text x="20" y="117">03</text></g>
  </svg>
  <div class="abs" style="left:38px;top:48px;width:65px;color:#fff"><b style="font-size:4.5px">Lorem Ipsum</b><p style="font-size:2.5px;line-height:1.4">Lorem ipsum dolor sit amet, consectetur adipiscing elit, sed do eiusmod tempor incididunt ut labore et.</p></div>
  <div class="abs" style="left:38px;top:76px;width:65px;color:#fff"><b style="font-size:4.5px">Lorem Ipsum</b><p style="font-size:2.5px;line-height:1.4">Lorem ipsum dolor sit amet, consectetur adipiscing elit, sed do eiusmod tempor incididunt ut labore et.</p></div>
  <div class="abs" style="left:38px;top:105px;width:65px;color:#fff"><b style="font-size:4.5px">Lorem Ipsum</b><p style="font-size:2.5px;line-height:1.4">Lorem ipsum dolor sit amet, consectetur adipiscing elit, sed do eiusmod tempor incididunt ut labore et.</p></div>
  <div class="abs" style="left:140px;top:46px;width:66px;color:#fff"><b style="font-size:4.5px">Lorem Ipsum</b><p style="font-size:2.5px;line-height:1.4">Lorem ipsum dolor sit amet, consectetur adipiscing elit, sed do eiusmod tempor incididunt ut labore et.</p></div>
  <div class="abs" style="left:140px;top:74px;width:66px;color:#fff"><b style="font-size:4.5px">Lorem Ipsum</b><p style="font-size:2.5px;line-height:1.4">Lorem ipsum dolor sit amet, consectetur adipiscing elit, sed do eiusmod tempor incididunt ut labore et.</p></div>
  <div class="abs" style="left:140px;top:103px;width:66px;color:#fff"><b style="font-size:4.5px">Lorem Ipsum</b><p style="font-size:2.5px;line-height:1.4">Lorem ipsum dolor sit amet, consectetur adipiscing elit, sed do eiusmod tempor incididunt ut labore et.</p></div>
  <p class="body" style="left:55px;top:134px;width:170px;text-align:center;font-size:2.7px">Lorem ipsum dolor sit amet, consectetur adipiscing elit, sed do eiusmod tempor incididunt ut labore et dolore magna aliqua. Ut enim ad minim veniam, quis nostrud exercitation ullamco laboris nisi ut aliquip ex ea commodo consequat.</p>
</section>

<!-- Slide 4: timeline -->
<section class="slide" style="left:896px;top:25px">
  <div class="brand" style="left:234px;top:7px"><span class="dot"></span>mapleforge</div>
  <svg style="left:54px;top:16px" width="9" height="9"><path d="M1 1h8v8M9 1L1 9" stroke="#3d3d42" stroke-width=".8" fill="none" transform="scale(-1 1) translate(-10 0)"/></svg>
  <div class="abs" style="left:70px;top:15px;font-family:Roboto,sans-serif;font-weight:700;font-size:11px;letter-spacing:3.2px;color:var(--ink)">TIMELINE <span style="color:var(--blue)">SLIDE</span></div>
  <div class="abs" style="left:108px;top:29px;width:56px;height:1px;background:var(--ink)"></div>
  <svg width="277" height="156">
    <g fill="none" stroke-width="5">
      <circle cx="48" cy="73" r="22" stroke="#5b3aa0"/>
      <circle cx="93" cy="73" r="22" stroke="#4a4db0"/>
      <circle cx="138" cy="73" r="22" stroke="#2f74cc"/>
      <circle cx="183" cy="73" r="22" stroke="#1e93dc"/>
      <circle cx="228" cy="73" r="22" stroke="#2aa9ea"/>
    </g>
    <g fill="none" stroke-width="1.8">
      <circle cx="48" cy="73" r="13" stroke="#5b3aa0"/><circle cx="93" cy="73" r="13" stroke="#4a4db0"/><circle cx="138" cy="73" r="13" stroke="#2f74cc"/><circle cx="183" cy="73" r="13" stroke="#1e93dc"/><circle cx="228" cy="73" r="13" stroke="#2aa9ea"/>
    </g>
    <g stroke="#3d3d42" stroke-width=".6"><path d="M42 134h12M87 134h12M132 134h12M177 134h12M222 134h12"/></g>
  </svg>
  <div class="caption" style="left:26px;top:105px;width:44px">Lorem ipsum dolor sit amet, consectetur adipiscing elit, sed do eiusmod tempor</div>
  <div class="caption" style="left:71px;top:105px;width:44px">Lorem ipsum dolor sit amet, consectetur adipiscing elit, sed do eiusmod tempor</div>
  <div class="caption" style="left:116px;top:105px;width:44px">Lorem ipsum dolor sit amet, consectetur adipiscing elit, sed do eiusmod tempor</div>
  <div class="caption" style="left:161px;top:105px;width:44px">Lorem ipsum dolor sit amet, consectetur adipiscing elit, sed do eiusmod tempor</div>
  <div class="caption" style="left:206px;top:105px;width:44px">Lorem ipsum dolor sit amet, consectetur adipiscing elit, sed do eiusmod tempor</div>
</section>

<!-- Slide 5: section divider -->
<section class="slide" style="left:26px;top:194px;background:linear-gradient(135deg,#1a6fd0,#1d9ae4 60%,#1478cf)">
  <div class="abs" role="img" aria-label="Faint binary code and cloud texture" style="inset:0;background:radial-gradient(ellipse at 45% 35%,rgba(150,215,255,.35),rgba(0,0,0,0) 60%)"></div>
  <div class="abs" style="left:14px;top:16px;width:249px;height:126px;border:1px solid #fff"></div>
  <svg style="left:250px;top:20px" width="9" height="9"><path d="M1 1h8v8M9 1L1 9" stroke="#fff" stroke-width=".8" fill="none"/></svg>
  <div class="abs" style="left:63px;top:53px;width:1px;height:50px;background:#fff"></div>
  <div class="abs" style="left:0;width:277px;top:59px;text-align:center;color:#fff;font-family:Roboto,sans-serif;font-weight:900;font-size:15px">BUSINESS SLIDE</div>
  <p class="body white" style="left:68px;top:76px;width:150px;text-align:center;font-size:3px">Lorem ipsum dolor sit amet, consectetur adipiscing elit, sed do eiusmod tempor incididunt ut labore et dolore magna aliqua. Ut enim ad minim veniam, quis nostrud exercitation ullamco laboris</p>
  <p class="body white" style="left:68px;top:92px;width:150px;text-align:center;font-size:3px">Lorem ipsum dolor sit amet, consectetur adipiscing elit, sed do.</p>
  <div class="brand light" style="left:108px;top:116px;font-size:9px;gap:3px"><span class="dot" style="width:7px;height:7px"></span>mapleforge</div>
</section>

<!-- Slide 6: pricing -->
<section class="slide" style="left:316px;top:194px">
  <div class="brand" style="left:234px;top:7px"><span class="dot"></span>mapleforge</div>
  <div class="headline" style="left:11px;top:32px">Head<span>Line</span></div>
  <p class="body" style="left:11px;top:47px;width:72px">Lorem ipsum dolor sit amet, consectetur adipiscing elit, sed do eiusmod tempor incididunt ut labore et dolore magna aliqua. Ut enim ad minim veniam, quis nostrud exercitation ullamco laboris nisi ut aliquip ex ea commodo consequat. Duis aute irure dolor in reprehenderit in voluptate velit esse cillum dolore eu fugiat nulla pariatur. Excepteur sint occaecat cupidatat non proident, sunt in culpa qui officia deserunt mollit anim id est laborum.</p>
  <div class="button" style="left:11px;top:103px;width:70px">Lorem ipsum dolor sit amet, consectetur adipiscing elit, sed do eiusmod tempor aliqua.</div>
  <div class="abs" style="left:95px;top:31px;width:56px;height:17px;background:#2ba3e6;color:#fff;font-size:7px;text-align:center;line-height:17px">9.99$</div>
  <div class="abs" style="left:95px;top:48px;width:56px;height:65px;background:var(--grey)"></div>
  <div class="abs" style="left:151px;top:15px;width:56px;height:23px;background:#1fb4e6;color:#fff;font-size:7px;text-align:center;line-height:23px">100$</div>
  <div class="abs" style="left:151px;top:38px;width:56px;height:82px;background:#ededef"></div>
  <div class="abs" style="left:207px;top:31px;width:56px;height:17px;background:#8fd6ee;color:#fff;font-size:7px;text-align:center;line-height:17px">200$</div>
  <div class="abs" style="left:207px;top:48px;width:56px;height:65px;background:var(--grey)"></div>
  <div class="caption" style="left:100px;top:58px;width:46px;font-size:2.8px">Lorem ipsum dolor sit amet, consectetur adipiscing elit, sed do eiusmod tempor</div>
  <div class="caption" style="left:156px;top:58px;width:46px;font-size:2.8px">Lorem ipsum dolor sit amet, consectetur adipiscing elit, sed do eiusmod tempor</div>
  <div class="caption" style="left:212px;top:58px;width:46px;font-size:2.8px">Lorem ipsum dolor sit amet, consectetur adipiscing elit, sed do eiusmod tempor</div>
  <svg width="277" height="156"><g stroke="#3d3d42" stroke-width=".5"><path d="M118 81h10M174 81h10M230 81h10"/></g></svg>
  <p class="body" style="left:100px;top:87px;width:46px;text-align:center;font-size:2px">Lorem ipsum dolor sit amet, consectetur adipiscing elit, sed do eiusmod tempor incididunt ut labore et dolore magna aliqua.</p>
  <p class="body" style="left:156px;top:87px;width:46px;text-align:center;font-size:2px">Lorem ipsum dolor sit amet, consectetur adipiscing elit, sed do eiusmod tempor incididunt ut labore et dolore magna aliqua.</p>
  <p class="body" style="left:212px;top:87px;width:46px;text-align:center;font-size:2px">Lorem ipsum dolor sit amet, consectetur adipiscing elit, sed do eiusmod tempor incididunt ut labore et dolore magna aliqua.</p>
  <p class="body" style="left:95px;top:130px;width:168px;text-align:center;font-size:2.7px">Lorem ipsum dolor sit amet, consectetur adipiscing elit, sed do eiusmod tempor incididunt ut labore et dolore magna aliqua. Ut enim ad minim veniam, quis nostrud exercitation ullamco laboris nisi ut aliquip ex ea commodo consequat.</p>
</section>

<!-- Slide 7: headline with swirl -->
<section class="slide" style="left:607px;top:194px">
  <div class="bar" style="left:16px;top:17px;width:92px;height:17px">Lorem ipsum dolor sit amet, consectetur adipiscing elit, sed do eiusmod tempor aliqua.</div>
  <svg style="left:96px;top:21px" width="9" height="9"><path d="M1 1h8v8M9 1L1 9" stroke="#fff" stroke-width=".8" fill="none"/></svg>
  <div class="headline" style="left:16px;top:49px">Head<span>Line</span></div>
  <p class="body" style="left:16px;top:64px;width:66px">Lorem ipsum dolor sit amet, consectetur adipiscing elit, sed do eiusmod tempor incididunt ut labore et dolore magna aliqua. Ut enim ad minim veniam, quis nostrud exercitation ullamco laboris nisi ut aliquip ex ea commodo consequat. Duis aute irure dolor in reprehenderit in voluptate velit esse cillum dolore eu fugiat nulla pariatur. Excepteur sint occaecat cupidatat non proident, sunt in culpa qui officia deserunt mollit anim id est laborum.</p>
  <div class="button" style="left:16px;top:121px;width:70px">Lorem ipsum dolor sit amet, consectetur adipiscing elit, sed do eiusmod tempor aliqua.</div>
  <div class="abs" role="img" aria-label="Large swirling blue graphic" style="left:135px;top:0;width:142px;height:156px;background:radial-gradient(circle at 62% 55%,#ffffff 0 18%,#9cd9ef 34%,#3fb5e6 58%,rgba(255,255,255,0) 75%)"></div>
</section>

<!-- Slide 8: team grid -->
<section class="slide" style="left:896px;top:194px">
  <div class="abs" style="left:16px;top:17px;width:60px;height:123px;background:#1f8bd6"></div>
  <div class="headline" style="left:19px;top:41px;color:#fff;font-size:11.5px">HeadLine</div>
  <p class="body white" style="left:19px;top:54px;width:54px;font-size:2.8px">Lorem ipsum dolor sit amet, consectetur adipiscing elit, sed do eiusmod tempor incididunt ut labore et dolore magna aliqua. Ut enim ad minim veniam, quis nostrud exercitation ullamco laboris nisi ut aliquip ex ea commodo consequat. Duis aute irure dolor in reprehenderit in voluptate velit esse cillum dolore eu fugiat nulla pariatur. Excepteur sint occaecat cupidatat non proident, sunt in culpa qui officia deserunt mollit anim id est laborum.</p>
  <svg style="left:19px;top:127px" width="9" height="9"><path d="M1 1h8v8M9 1L1 9" stroke="#fff" stroke-width=".8" fill="none" transform="scale(-1 1) translate(-10 0)"/></svg>
  <div class="abs" role="img" aria-label="Team member photo" style="left:77px;top:17px;width:61px;height:61px;background:linear-gradient(135deg,#6e9fb6,#8fb0c4)"></div>
  <div class="abs" role="img" aria-label="Team member photo" style="left:139px;top:17px;width:62px;height:61px;background:linear-gradient(135deg,#6a5e98,#8c84b4)"></div>
  <div class="abs" role="img" aria-label="Team member photo" style="left:202px;top:17px;width:61px;height:61px;background:linear-gradient(135deg,#6b8eb4,#8ba6c4)"></div>
  <div class="abs" role="img" aria-label="Team member photo" style="left:77px;top:79px;width:61px;height:61px;background:linear-gradient(135deg,#6a86b0,#7f8fb8)"></div>
  <div class="abs" role="img" aria-label="Team member photo" style="left:139px;top:79px;width:62px;height:61px;background:linear-gradient(135deg,#6fa0ba,#86a8c4)"></div>
  <div class="abs" role="img" aria-label="Team member photo" style="left:202px;top:79px;width:61px;height:61px;background:linear-gradient(135deg,#6a5a9c,#7e6eae)"></div>
</section>

<!-- Slide 9: percentages -->
<section class="slide" style="left:26px;top:363px">
  <div class="brand" style="left:234px;top:3px"><span class="dot"></span>mapleforge</div>
  <div class="title-caps" style="left:20px;top:10px">MAPLEFORGE DELIVERS YOUR ENTERPRISE<br>TECHNOLOGY GOALS!</div>
  <svg width="277" height="156">
    <g fill="none" stroke-width="1.5">
      <circle cx="45" cy="61" r="23" stroke="#5b3aa0"/>
      <circle cx="106" cy="61" r="23" stroke="#4a4db0"/>
      <circle cx="168" cy="61" r="23" stroke="#2f74cc"/>
      <circle cx="232" cy="61" r="23" stroke="#1e93dc"/>
    </g>
    <g fill="#1e6fcf"><circle cx="61" cy="45" r="6"/><circle cx="122" cy="45" r="6"/><circle cx="184" cy="45" r="6"/><circle cx="248" cy="45" r="6"/></g>
    <g fill="#fff"><circle cx="61" cy="45" r="2.5"/><circle cx="122" cy="45" r="2.5"/><circle cx="184" cy="45" r="2.5"/><circle cx="248" cy="45" r="2.5"/></g>
    <g font-family="Roboto" font-weight="700" font-size="8" fill="#3d3d42" text-anchor="middle"><text x="45" y="64">50%</text><text x="106" y="64">40%</text><text x="168" y="64">30%</text><text x="232" y="64">60%</text></g>
    <g stroke="#3d3d42" stroke-width=".5"><path d="M39 121h12M100 121h12M162 121h12M226 121h12"/></g>
  </svg>
  <div class="caption" style="left:23px;top:95px;width:44px">Lorem ipsum dolor sit amet, consectetur adipiscing elit, sed do eiusmod tempor</div>
  <div class="caption" style="left:84px;top:95px;width:44px">Lorem ipsum dolor sit amet, consectetur adipiscing elit, sed do eiusmod tempor</div>
  <div class="caption" style="left:146px;top:95px;width:44px">Lorem ipsum dolor sit amet, consectetur adipiscing elit, sed do eiusmod tempor</div>
  <div class="caption" style="left:210px;top:95px;width:44px">Lorem ipsum dolor sit amet, consectetur adipiscing elit, sed do eiusmod tempor</div>
  <p class="body" style="left:23px;top:127px;width:44px;text-align:center;font-size:2px">Lorem ipsum dolor sit amet, consectetur adipiscing elit, sed do eiusmod tempor incididunt ut labore et dolore magna aliqua.</p>
  <p class="body" style="left:84px;top:127px;width:44px;text-align:center;font-size:2px">Lorem ipsum dolor sit amet, consectetur adipiscing elit, sed do eiusmod tempor incididunt ut labore et dolore magna aliqua.</p>
  <p class="body" style="left:146px;top:127px;width:44px;text-align:center;font-size:2px">Lorem ipsum dolor sit amet, consectetur adipiscing elit, sed do eiusmod tempor incididunt ut labore et dolore magna aliqua.</p>
  <p class="body" style="left:210px;top:127px;width:44px;text-align:center;font-size:2px">Lorem ipsum dolor sit amet, consectetur adipiscing elit, sed do eiusmod tempor incididunt ut labore et dolore magna aliqua.</p>
</section>

<!-- Slide 10: donut schedule -->
<section class="slide" style="left:316px;top:363px">
  <div class="brand" style="left:234px;top:3px"><span class="dot"></span>mapleforge</div>
  <div class="bar" style="left:15px;top:17px;width:93px;height:17px">Lorem ipsum dolor sit amet, consectetur adipiscing elit, sed do eiusmod tempor aliqua.</div>
  <svg style="left:96px;top:21px" width="9" height="9"><path d="M1 1h8v8M9 1L1 9" stroke="#fff" stroke-width=".8" fill="none"/></svg>
  <div class="headline" style="left:15px;top:50px">Head<span>Line</span></div>
  <p class="body" style="left:15px;top:65px;width:66px">Lorem ipsum dolor sit amet, consectetur adipiscing elit, sed do eiusmod tempor incididunt ut labore et dolore magna aliqua. Ut enim ad minim veniam, quis nostrud exercitation ullamco laboris nisi ut aliquip ex ea commodo consequat. Duis aute irure dolor in reprehenderit in voluptate velit esse cillum dolore eu fugiat nulla pariatur. Excepteur sint occaecat cupidatat non proident, sunt in culpa qui officia deserunt mollit anim id est laborum.</p>
  <div class="button" style="left:15px;top:122px;width:70px">Lorem ipsum dolor sit amet, consectetur adipiscing elit, sed do eiusmod tempor aliqua.</div>
  <svg width="277" height="156">
    <g fill="none" stroke-width="12">
      <path d="M190 39 A30 30 0 0 1 220 69" stroke="#4a4db0"/>
      <path d="M220 69 A30 30 0 0 1 190 99" stroke="#2f74cc"/>
      <path d="M190 99 A30 30 0 0 1 160 69" stroke="#1e93dc"/>
      <path d="M160 69 A30 30 0 0 1 190 39" stroke="#5b3aa0"/>
    </g>
    <circle cx="190" cy="69" r="11" fill="#3fb5e6"/>
    <g fill="none" stroke="#3d3d42" stroke-width=".5">
      <path d="M125 38h30l10 12M125 96h30l10-12M255 38h-28l-10 12M255 96h-28l-10-12"/>
    </g>
    <g font-family="Roboto" font-size="6" fill="#3d3d42">
      <text x="132" y="36">20:13</text><text x="235" y="36">13:25</text>
      <text x="132" y="104">19:10</text><text x="235" y="104">16:00</text>
    </g>
  </svg>
  <p class="body" style="left:122px;top:40px;width:30px;font-size:2.3px">Lorem ipsum dolor sit amet, consectetur adipiscing elit, sed do eiusmod tempor incididunt ut labore et dolore magna aliqua.</p>
  <p class="body" style="left:229px;top:40px;width:30px;font-size:2.3px">Lorem ipsum dolor sit amet, consectetur adipiscing elit, sed do eiusmod tempor incididunt ut labore et dolore magna aliqua.</p>
  <p class="body" style="left:122px;top:74px;width:30px;font-size:2.3px">Lorem ipsum dolor sit amet, consectetur adipiscing elit, sed do eiusmod tempor incididunt ut labore et dolore magna aliqua.</p>
  <p class="body" style="left:229px;top:74px;width:30px;font-size:2.3px">Lorem ipsum dolor sit amet, consectetur adipiscing elit, sed do eiusmod tempor incididunt ut labore et dolore magna aliqua.</p>
  <p class="body" style="left:128px;top:114px;width:128px;font-size:2.5px">Lorem ipsum dolor sit amet, consectetur adipiscing elit, sed do eiusmod tempor incididunt ut labore et dolore magna aliqua. Ut enim ad minim veniam, quis nostrud exercitation ullamco laboris nisi ut aliquip ex ea commodo consequat. Duis aute irure dolor in reprehenderit in voluptate velit esse cillum dolore eu fugiat nulla pariatur. Excepteur sint occaecat cupidatat non proident.</p>
  <div class="brand" style="left:234px;top:143px"><span class="dot"></span>mapleforge</div>
</section>

<!-- Slide 11: three-column band -->
<section class="slide" style="left:607px;top:363px">
  <div class="brand" style="left:234px;top:3px"><span class="dot"></span>mapleforge</div>
  <div class="title-caps" style="left:17px;top:21px">MAPLEFORGE DELIVERS YOUR ENTERPRISE<br>TECHNOLOGY GOALS!</div>
  <div class="abs" style="left:0;top:48px;width:93px;height:57px;background:#2b9fe2"></div>
  <div class="abs" style="left:93px;top:48px;width:93px;height:57px;background:#2fb2e6"></div>
  <div class="abs" style="left:186px;top:48px;width:91px;height:57px;background:#8fd0e8"></div>
  <p class="body white" style="left:19px;top:62px;width:54px;font-size:2.3px">Lorem ipsum dolor sit amet, consectetur adipiscing elit, sed do eiusmod tempor incididunt ut labore et dolore magna aliqua. Ut enim ad minim veniam.</p>
  <p class="body white" style="left:19px;top:80px;width:54px;font-size:2.3px">Lorem ipsum dolor sit amet, consectetur adipiscing elit, sed do eiusmod tempor incididunt ut labore et dolore magna aliqua. Ut enim ad minim veniam.</p>
  <p class="body white" style="left:113px;top:62px;width:54px;font-size:2.3px">Lorem ipsum dolor sit amet, consectetur adipiscing elit, sed do eiusmod tempor incididunt ut labore et dolore magna aliqua. Ut enim ad minim veniam.</p>
  <p class="body white" style="left:113px;top:80px;width:54px;font-size:2.3px">Lorem ipsum dolor sit amet, consectetur adipiscing elit, sed do eiusmod tempor incididunt ut labore et dolore magna aliqua. Ut enim ad minim veniam.</p>
  <div class="headline" style="left:210px;top:68px;color:#fff;font-size:8px">HeadLine</div>
  <p class="body white" style="left:210px;top:77px;width:48px;font-size:2.2px">Lorem ipsum dolor sit amet, consectetur adipiscing elit, sed do eiusmod tempor.</p>
  <p class="body" style="left:58px;top:116px;width:165px;text-align:center;font-size:2.7px">Lorem ipsum dolor sit amet, consectetur adipiscing elit, sed do eiusmod tempor incididunt ut labore et dolore magna aliqua. Ut enim ad minim veniam, quis nostrud exercitation ullamco laboris nisi ut aliquip ex ea commodo consequat.</p>
  <div class="brand" style="left:234px;top:143px"><span class="dot"></span>mapleforge</div>
</section>

<!-- Slide 12: contact -->
<section class="slide" style="left:896px;top:363px;background:linear-gradient(135deg,#1b7fd3,#1a9ae2)">
  <div class="abs" role="img" aria-label="Faint circuit-line texture" style="inset:0;background:radial-gradient(ellipse at 30% 40%,rgba(120,200,250,.3),rgba(0,0,0,0) 60%)"></div>
  <div class="brand light" style="left:90px;top:44px;font-size:11px;gap:3px"><span class="dot" style="width:8px;height:8px"></span>mapleforge</div>
  <div class="abs" style="left:0;width:277px;top:67px;text-align:center;color:#fff;font-family:Roboto,sans-serif;font-weight:700;font-size:6.5px;letter-spacing:1.6px">ContatUs</div>
  <div class="abs" style="left:66px;top:79px;color:#fff;font-size:4px;line-height:1.45;font-weight:600">tel. +15550142071<br>tel. +15550163382<br>tel. +15550187494</div>
  <div class="abs" style="left:150px;top:79px;color:#fff;font-size:4px;line-height:1.45;font-weight:600">hello@mapleforge-mail.com<br>hello@mapleforge-mail.com<br>hello@mapleforge-mail.com</div>
  <p class="body white" style="left:78px;top:106px;width:122px;text-align:center;font-size:2.5px">Lorem ipsum dolor sit amet, consectetur adipiscing elit, sed do eiusmod tempor incididunt ut labore et dolore magna aliqua.</p>
</section>

</body>
</html>
```